Lagoon Canopy NZ Product Catalogue

To redesign our suppliers catalogue and make it my own.
Vertrano is our supplier, although now I want a "Lagoon Canopy NZ" catalogue, with an updated look as well.

I have attached our logos, Vertrano catalogue and a few photos of completed work (which may need editing to look better).

Also pages I want to use from the catalogue (be similar to) are page numbers:
10 - 21 (products we sell)
It will also need a cover and contents page and a commercial enclosure page after the other products (with commercial 1 and 20130422_1 photos).

The first page as you open the catalogue I want the about us section of our website on there www.lagooncanopy.co.nz (two sections "what we offer" and "enclosure advantages")

If you need better photos or more information please contact me on:
warren@lagooncanopy.co.nz

Contact details: Toll Free 0508 SUNDOMES (786 366) Email sales@lagooncanopy.co.nz

Industry/Entity Type

Construction

Colors

Designer to choose colors to be used in the design.

Requirements
Must have
• Must have double sided pages,
• With each different design to have two pages which open together.
• The standard sizing which is in the Vertrano Catalogue must be there.
• Designs are: Marrakesh Horizon, Marrakesh, Tropik, Denver, Verona and Extra Shelters
• Must be printable and pdf sendable.
• Use "What we offer" and "Enclosure Advantages" to the first page customer opens to, maybe also a contents page.
• Also please add to the "enclosure advantages" bullet point list "Year-round average of 8 degree warmer water"
Nice to have
• Would be nice to have the custom sizing box as well on the designs asked for.
• Also a Commercial section after the rest of the designs using the "commercial 1" and "20130422_1" photos
• The more photos the better
• Be nice to be high resolution and I want to print it in a gloss finish.
• Also A4 size would be nice, but A5 will work also
Should not have
• Marrakesh Horizon Neo and try and minimise the Vertrano branding

```html
<!DOCTYPE html>
<html lang="en">
<head>
<meta charset="utf-8">
<title>Lagoon Canopy NZ – Catalogue Cover Spread</title>
<link href="https://fonts.googleapis.com/css2?family=Bebas+Neue&family=Montserrat:wght@400;700&family=Open+Sans:wght@400&display=swap" rel="stylesheet">
<style>
  :root{
    --stage:#7b7b7b;
    --paper:#ffffff;
    --paper-tint:#f1f1f2;
    --brand-blue:#1f5fa8;
    --heading-blue:#3f86c8;
    --ink:#2a2a2a;
    --ghost:#ededee;
    --ghost-line:#e2e2e4;
    --water-deep:#1b8fb0;
    --water-light:#7fd3e3;
  }
  *{box-sizing:border-box;margin:0;padding:0}
  html,body{width:902px;height:1200px;overflow:hidden;background:var(--stage)}
  .spread{
    position:absolute;left:21px;top:296px;width:860px;height:608px;
    background:var(--paper);box-shadow:0 8px 18px rgba(0,0,0,.35);overflow:hidden;
  }
  .back-cover{position:absolute;left:0;top:0;width:430px;height:608px;background:var(--paper)}
  .front-cover{position:absolute;left:430px;top:0;width:430px;height:608px;background:var(--paper-tint)}
  .front-cover .footer-band{position:absolute;left:0;bottom:0;width:430px;height:123px;background:var(--paper)}

  .ghost-name{
    position:absolute;left:48px;top:580px;transform-origin:left top;transform:rotate(-90deg);
    font-family:'Montserrat',sans-serif;font-weight:700;font-size:38px;letter-spacing:1px;
    color:var(--ghost);white-space:nowrap;
  }
  .ghost-boxes{position:absolute;left:135px;top:420px}

  .contact{position:absolute;left:140px;top:268px;width:140px;text-align:center;font-family:'Montserrat',sans-serif}
  .contact-title{font-size:10.5px;color:var(--ink);font-weight:400}
  .contact-title strong{color:var(--heading-blue);font-weight:700}
  .contact-rule{width:22px;height:1px;background:var(--heading-blue);margin:4px auto 0}
  .contact-icons{display:flex;justify-content:center;gap:8px;margin:14px 0 10px}
  .contact-lines{font-size:9.5px;line-height:16px;color:var(--ink)}

  .pocket-notch{position:absolute;left:297px;top:283px;width:24px;height:24px;border-radius:50%;
    background:var(--paper);border:1px solid #e4e4e4}

  .cover-photo{
    position:absolute;left:309px;top:116px;width:551px;height:369px;
    background:linear-gradient(160deg,var(--water-light) 0%,var(--water-deep) 60%,#2aa5c2 100%);
  }

  .brand-name{
    position:absolute;left:480px;top:42px;width:330px;
    display:flex;align-items:center;justify-content:center;gap:10px;
    font-family:'Montserrat',sans-serif;font-weight:700;font-size:26px;color:var(--brand-blue);letter-spacing:.5px;
  }
  .brand-dot{width:14px;height:14px;border-radius:50%;background:var(--brand-blue);flex:none}

  .cover-headline{position:absolute;left:430px;top:497px;width:430px;text-align:center;
    font-family:'Bebas Neue',sans-serif;font-weight:400;font-size:35px;letter-spacing:.3px;color:var(--heading-blue)}
  .cover-subline{position:absolute;left:430px;top:538px;width:430px;text-align:center;
    font-family:'Open Sans',sans-serif;font-size:10.5px;color:var(--ink)}
  .cover-url{position:absolute;left:430px;top:580px;width:430px;text-align:center;
    font-family:'Open Sans',sans-serif;font-size:8.5px;letter-spacing:3px;color:var(--ink)}
</style>
</head>
<body>
  <div class="spread">
    <section class="back-cover">
      <div class="ghost-name">LAGOON CANOPY NZ</div>
      <svg class="ghost-boxes" width="270" height="150" viewBox="0 0 270 150" fill="none" stroke="var(--ghost-line)" stroke-width="1.5">
        <rect x="95" y="5" width="68" height="68"/>
        <rect x="160" y="42" width="40" height="40"/>
        <rect x="20" y="58" width="10" height="10"/>
        <rect x="42" y="66" width="30" height="72"/>
        <rect x="72" y="66" width="68" height="76"/>
        <rect x="140" y="82" width="24" height="18"/>
        <rect x="160" y="82" width="70" height="62"/>
      </svg>

      <div class="contact">
        <div class="contact-title"><strong>CONTACT</strong> US</div>
        <div class="contact-rule"></div>
        <div class="contact-icons">
          <svg width="14" height="14" viewBox="0 0 14 14" fill="none" stroke="var(--heading-blue)" stroke-width="1.1"><circle cx="7" cy="7" r="6.2"/><path d="M5.2 4.2c-.8.6-.6 2 .4 3.4s2.2 2.2 3 1.8l.4-.8-1.2-.8-.6.4c-.5-.2-1.2-1-1.4-1.6l.5-.6-.6-1.3z"/></svg>
          <svg width="14" height="14" viewBox="0 0 14 14" fill="none" stroke="var(--heading-blue)" stroke-width="1.1"><circle cx="7" cy="7" r="6.2"/><rect x="3.8" y="4.8" width="6.4" height="4.4"/><path d="M3.8 4.8 7 7.4l3.2-2.6"/></svg>
          <svg width="14" height="14" viewBox="0 0 14 14" fill="none" stroke="var(--heading-blue)" stroke-width="1.1"><circle cx="7" cy="7" r="6.2"/><circle cx="7" cy="7" r="3.4"/><path d="M3.6 7h6.8M7 3.6c-1.5 2-1.5 4.8 0 6.8M7 3.6c1.5 2 1.5 4.8 0 6.8"/></svg>
        </div>
        <div class="contact-lines">
          0214865120<br>
          warren@lagooncanopy.co.nz<br>
          www.lagooncanopy.co.nz
        </div>
      </div>
    </section>

    <section class="front-cover">
      <div class="footer-band"></div>
    </section>

    <div class="cover-photo" role="img" aria-label="Photo of a child floating on a rainbow kickboard in a sunlit pool"></div>
    <div class="pocket-notch"></div>

    <div class="brand-name"><span class="brand-dot"></span>LAGOON CANOPY NZ</div>

    <h1 class="cover-headline">Increased Water Temperature</h1>
    <p class="cover-subline">Free Heating From The Sun, Providing Significant Savings</p>
    <p class="cover-url">www.lagooncanopy.co.nz</p>
  </div>
</body>
</html>
```